Simply Brochure Design Project

I need a simple 1 page sales brochure must include 8 images and some simple text which i can provide, need this asap.

We have the best range of printed luggage in Australia with a built in tracking system and limited edition designs.

On the attached poster you will see the info for the bullet points, on the bottom of the new poster id also like, Top up in Singles...

plus To Order email trapley@brookvane.com.au or call 02 9417 2683

Target Market(s)

Luggage store owners

Industry/Entity Type

Call

Requirements
Must have
• 8/9 images

```html
<!DOCTYPE html>
<html lang="en">
<head>
<meta charset="utf-8">
<title>Printed Luggage Range – Sales Brochure</title>
<link href="https://fonts.googleapis.com/css2?family=Open+Sans:ital,wght@0,400;0,600;0,700;1,600&display=swap" rel="stylesheet">
<style>
  :root {
    --bg-top: #ffffff;
    --bg-bottom: #e4e6e9;
    --ink: #111111;
    --accent-blue: #1a6fc4;
    --banner-blue: #1f6fc5;
    --banner-light: #5aa2e6;
    --white: #ffffff;
  }
  * { box-sizing: border-box; margin: 0; padding: 0; }
  html, body { width: 912px; height: 1200px; overflow: hidden; }
  body {
    font-family: "Open Sans", Arial, sans-serif;
    background: linear-gradient(180deg, var(--bg-top) 0%, var(--bg-top) 35%, var(--bg-bottom) 100%);
    position: relative;
    color: var(--ink);
  }
  .brochure { position: relative; width: 912px; height: 1200px; }

  .case {
    position: absolute;
    border-radius: 18px;
    box-shadow: 0 8px 14px rgba(0,0,0,0.25);
  }
  .case-sky      { left: 302px; top: 82px;  width: 215px; height: 368px; background: linear-gradient(180deg, #2f7fd6 0%, #9cc8ee 45%, #d84a6a 75%, #e8963a 100%); z-index: 1; }
  .case-flag     { left: 119px; top: 258px; width: 239px; height: 372px; background: linear-gradient(135deg, #1f3d73 0%, #a7392f 45%, #d6b27e 60%, #213f78 100%); z-index: 2; }
  .case-flower   { left: 525px; top: 255px; width: 242px; height: 375px; background: radial-gradient(circle at 55% 45%, #7a4a12 0%, #e8a810 30%, #f6cc1c 70%, #e2a10e 100%); z-index: 2; }
  .case-speaker  { left: 30px;  top: 352px; width: 198px; height: 316px; background: radial-gradient(circle at 50% 50%, #2c6bd4 0%, #1c2e52 30%, #2a2622 55%, #151412 100%); z-index: 3; }
  .case-storage  { left: 241px; top: 447px; width: 136px; height: 228px; background: linear-gradient(180deg, #e4e0d8 0%, #c9c3b6 100%); z-index: 3; }
  .case-slogan   { left: 387px; top: 450px; width: 138px; height: 225px; background: linear-gradient(180deg, #1c1c1c 0%, #050505 100%); z-index: 3; }
  .case-stripes  { left: 532px; top: 447px; width: 136px; height: 228px; background: linear-gradient(135deg, #f2f2f2 0%, #6b6b6b 50%, #efefef 100%); z-index: 3; }
  .case-tower    { left: 682px; top: 333px; width: 208px; height: 339px; background: linear-gradient(180deg, #f4f4f4 0%, #9a9a9a 55%, #3a3a3a 100%); z-index: 3; }

  .guarantee-badge {
    position: absolute;
    left: 632px; top: 27px;
    width: 262px; height: 262px;
    z-index: 5;
  }

  .feature-list {
    position: absolute;
    left: 57px; top: 698px;
    list-style: none;
  }
  .feature-list li {
    position: relative;
    padding-left: 18px;
    font-size: 27px;
    height: 60px;
    line-height: 60px;
    letter-spacing: -0.2px;
    white-space: nowrap;
  }
  .feature-list li::before {
    content: "";
    position: absolute;
    left: 0; top: 50%;
    width: 7px; height: 7px;
    border-radius: 50%;
    background: var(--accent-blue);
    transform: translateY(-50%);
  }
  .highlight {
    color: var(--accent-blue);
    font-weight: 600;
    font-size: 32px;
  }

  .order-banner {
    position: absolute;
    left: 0; top: 1074px;
    width: 712px; height: 118px;
    background: linear-gradient(90deg, var(--banner-blue) 0%, var(--banner-blue) 55%, var(--banner-light) 100%);
    clip-path: polygon(0 0, 96% 0, 100% 100%, 0 100%);
    display: flex;
    flex-direction: column;
    justify-content: center;
    align-items: center;
    padding-right: 20px;
    color: var(--white);
    font-style: italic;
    font-weight: 600;
    font-size: 24px;
    line-height: 33px;
    letter-spacing: 0.8px;
  }
  .order-banner p { white-space: nowrap; }
</style>
</head>
<body>
<main class="brochure">
  <div class="case case-sky" role="img" aria-label="Suitcase printed with blue sky, clouds and tulips"></div>
  <div class="case case-flag" role="img" aria-label="Suitcase printed with a vintage flag design"></div>
  <div class="case case-flower" role="img" aria-label="Suitcase printed with a sunflower close-up"></div>
  <div class="case case-speaker" role="img" aria-label="Suitcase printed with a loudspeaker design"></div>
  <div class="case case-storage" role="img" aria-label="Suitcase printed with a stencilled storage crate design"></div>
  <div class="case case-slogan" role="img" aria-label="Black suitcase printed with a bold slogan"></div>
  <div class="case case-stripes" role="img" aria-label="Suitcase printed with a zebra stripe pattern"></div>
  <div class="case case-tower" role="img" aria-label="Suitcase printed with a black and white tower photograph"></div>

  <svg class="guarantee-badge" viewBox="0 0 262 262" aria-label="5 Year Guarantee">
    <defs>
      <radialGradient id="badgeFill" cx="50%" cy="45%" r="60%">
        <stop offset="0%" stop-color="#e0241a"/>
        <stop offset="100%" stop-color="#8e0a06"/>
      </radialGradient>
    </defs>
    <g fill="url(#badgeFill)">
      <rect x="38" y="38" width="186" height="186"/>
      <rect x="38" y="38" width="186" height="186" transform="rotate(15 131 131)"/>
      <rect x="38" y="38" width="186" height="186" transform="rotate(30 131 131)"/>
      <rect x="38" y="38" width="186" height="186" transform="rotate(45 131 131)"/>
      <rect x="38" y="38" width="186" height="186" transform="rotate(60 131 131)"/>
      <rect x="38" y="38" width="186" height="186" transform="rotate(75 131 131)"/>
    </g>
    <text x="131" y="128" text-anchor="middle" fill="#ffffff" font-family="Open Sans, Arial, sans-serif" font-weight="700">
      <tspan font-size="62">5</tspan><tspan font-size="36" dx="8">Year</tspan>
    </text>
    <text x="131" y="172" text-anchor="middle" fill="#ffffff" font-family="Open Sans, Arial, sans-serif" font-weight="700" font-size="32">Guarantee</text>
  </svg>

  <ul class="feature-list">
    <li>Dutch Design With <span class="highlight">Limited Edition Prints</span></li>
    <li><span class="highlight">Extra Durable</span> Poly Carbonate ABS material</li>
    <li><span class="highlight">Luggage Tracking System</span> built in.. (Path Keeper)</li>
    <li><span class="highlight">Non Scratch Printing</span> Method</li>
    <li>Superior Smooth <span class="highlight">Japanese Racing Wheels</span></li>
    <li>Light weight and Super Strong</li>
  </ul>

  <footer class="order-banner">
    <p>Top up in Singles...</p>
    <p>To Order email trapley@brookvane.com.au</p>
    <p>or call 02 9417 2683</p>
  </footer>
</main>
</body>
</html>
```